Business Cards for a company that provides webstore services to veterinarians

We need business cards designed for our main service PawCartHub. PawCartHub is a webstore that veterinarian clinics can use to that will allow their clients to purchase products for their pets. Our company is Brivolta Veterinary Solutions (Brivolta Veterinary Solutions). Our mission statement is We love pets! We will do everything possible to facilitate along, healthy and happy relationship with their families.

Target Market(s)

Veterinarians

Industry/Entity Type

Veterinary

Contact Information for Business Card

I would like the design to incorporate the colours our our company. Cards should have room for employee name, title (only necessary in two instances), phone number, mobile number, email address and linkedin symbol and related profile name ie Moira Felton. I would like the PawCartHub logo to appear on one side and Brivolta Veterinary Solutions logo to appear on the other. I will need both an english and french version. I can provide the french translation. Please focus on english version and then we will translate

Colors

Designer to choose colors to be used in the design.

Requirements
Must have
• one side - PawCartHub logo with persons name, phone number, mobile number, email address
• second side - Brivolta Veterinary Solutions logo
• colours should be consistent with our company. colours are as follows:
• Red
• RGB: 190 / 30 / 45
• CYMK: 14 / 100 / 90 /10
• Hex: #BE1E2D
• Gray
• RGB: 88 / 89 / 86
• CYMK: 3 / 2 / 0 /64
• Hex: #585956
Nice to have
• address of company - can be on either side address is 4817 Quillan Street Suite 305 Burlington ON K9R 2M4. Toll free number will vary depending on person
• Linkedin symbol and name of person
• on second side with Brivolta Veterinary Solutions logo our company's mission statement
Should not have
• nothing comes to mind

```html
<!DOCTYPE html>
<html lang="en">
<head>
<meta charset="utf-8">
<title>PawCartHub / Brivolta Business Cards</title>
<link href="https://fonts.googleapis.com/css2?family=Source+Sans+3:wght@400;600;700&family=Arimo:wght@400&display=swap" rel="stylesheet">
<style>
  :root{
    --brand-red:#BE1E2D;
    --brand-gray:#585956;
    --card-white:#F4F3F1;
    --backdrop:#2F2A27;
  }
  *{margin:0;padding:0;box-sizing:border-box;}
  html,body{width:1200px;height:844px;overflow:hidden;}
  body{
    background:var(--backdrop);
    font-family:"Source Sans 3",Arial,sans-serif;
    position:relative;
  }
  .card{
    position:absolute;
    top:267px;
    width:540px;
    height:310px;
    background:var(--card-white);
    box-shadow:0 6px 18px rgba(0,0,0,.45);
  }
  .card--front{left:40px;}
  .card--back{left:620px;}

  /* front */
  .front-logo{
    position:absolute;
    top:62px;
    left:190px;
    display:flex;
    align-items:center;
    gap:10px;
  }
  .front-logo__name{
    font-size:44px;
    font-weight:600;
    color:var(--brand-red);
    letter-spacing:-.5px;
  }
  .front-logo__mark{
    width:14px;height:14px;border-radius:50%;
    background:var(--brand-red);
  }
  .holder{
    position:absolute;
    left:34px;
    top:170px;
  }
  .holder__name{
    font-size:19px;
    font-weight:700;
    color:var(--brand-red);
    text-transform:uppercase;
    letter-spacing:.3px;
  }
  .holder__title{
    font-size:15px;
    color:var(--brand-gray);
    margin-top:-2px;
  }
  .holder__address{
    font-size:15px;
    color:var(--brand-gray);
    margin-top:16px;
  }
  .contact-line{
    position:absolute;
    left:34px;
    bottom:30px;
    font-size:15px;
    color:var(--brand-gray);
    display:flex;
    gap:14px;
  }
  .contact-line__label{
    color:var(--brand-red);
    font-weight:700;
  }
  .social-square{
    position:absolute;
    right:30px;
    top:176px;
    width:22px;height:22px;
    background:var(--brand-red);
  }

  /* back */
  .back-logo{
    position:absolute;
    top:78px;
    left:0;right:0;
    display:flex;
    justify-content:center;
    align-items:center;
    gap:10px;
  }
  .back-logo__name{
    font-size:28px;
    font-weight:600;
    color:var(--brand-red);
    white-space:nowrap;
  }
  .back-logo__mark{
    width:12px;height:12px;border-radius:50%;
    background:var(--brand-red);
    flex:none;
  }
  .mission{
    position:absolute;
    top:168px;
    left:0;right:0;
    text-align:center;
    font-family:"Arimo",Arial,sans-serif;
    font-size:15px;
    line-height:1.3;
    color:var(--brand-red);
  }
</style>
</head>
<body>
  <section class="card card--front" aria-label="Business card front">
    <div class="front-logo">
      <span class="front-logo__name">PawCartHub</span>
      <span class="front-logo__mark"></span>
    </div>
    <div class="social-square" aria-hidden="true"></div>
    <div class="holder">
      <p class="holder__name">Dorian Pell</p>
      <p class="holder__title">Managing Director</p>
      <p class="holder__address">4817 Quillan Street Suite 305 Burlington ON K9R 2M4</p>
    </div>
    <p class="contact-line">
      <span><span class="contact-line__label">P:</span> (905)5550142</span>
      <span><span class="contact-line__label">M:</span> (905)5550142</span>
      <span><span class="contact-line__label">E:</span> info@pawcarthub.ca</span>
    </p>
  </section>

  <section class="card card--back" aria-label="Business card back">
    <div class="back-logo">
      <span class="back-logo__mark"></span>
      <span class="back-logo__name">Brivolta Veterinary Solutions</span>
    </div>
    <p class="mission">
      We love pets!<br>
      We will do everything possible to facilitate along,<br>
      healthy and happy relationship wih their families.
    </p>
  </section>
</body>
</html>
```